Business card for Internet Marketing Consultant

Simple - need a nice business card design using the logo elements and colors. Keywords: Progressive, professional, stylish, minimalist. Please use the kr as part of the design.

Info for card:

Gareth Pennock
Internet Marketing Strategist
Phone: (555) 813-2064
Email: gareth@korvantareach.com
Address: 2156 N. Halvern Ave., Ste. 118
Maplecrest, Nevada 89047

Website: www.korvantareach.com

Business

Sans Serif

```html
<!DOCTYPE html>
<html lang="en">
<head>
<meta charset="utf-8">
<title>Korvanta Reach – Business Card</title>
<link rel="stylesheet" href="https://fonts.googleapis.com/css2?family=Josefin+Sans:wght@400;700&family=Tinos:wght@400;700&display=swap">
<style>
  :root {
    --brand-green: #6bbf67;
    --brand-blue: #3a6db5;
    --ink: #111111;
    --grey-text: #8a8a8a;
    --paper: #ffffff;
    --backdrop: #e9e9e6;
  }
  * { box-sizing: border-box; margin: 0; padding: 0; }
  html, body { width: 1200px; height: 900px; overflow: hidden; }
  body {
    background: var(--backdrop);
    position: relative;
    font-family: "Josefin Sans", sans-serif;
  }
  .card {
    position: absolute;
    left: 320px;
    width: 560px;
    height: 320px;
    background: var(--paper);
    box-shadow: 0 6px 18px rgba(0,0,0,0.18);
    overflow: hidden;
  }
  .card--front { top: 100px; }
  .card--back { top: 480px; }

  /* Wordmark */
  .wordmark { position: absolute; display: flex; flex-direction: column; }
  .wordmark__row { display: flex; align-items: center; gap: 10px; }
  .wordmark__dot {
    width: 26px; height: 26px; border-radius: 50%;
    background: var(--brand-blue);
  }
  .wordmark__name {
    font-weight: 700;
    color: var(--brand-blue);
    letter-spacing: 0.5px;
  }
  .wordmark__tagline {
    color: var(--grey-text);
    text-transform: uppercase;
    letter-spacing: 2.5px;
    margin-top: 4px;
  }

  /* Front */
  .card--front .wordmark { left: 0; right: 0; top: 74px; align-items: center; }
  .card--front .wordmark__name { font-size: 40px; }
  .card--front .wordmark__tagline { font-size: 12px; margin-left: 36px; }
  .front__rule {
    position: absolute; left: 0; right: 0; top: 218px; height: 6px;
    background: var(--ink);
  }
  .front__band {
    position: absolute; left: 0; right: 0; top: 236px; bottom: 0;
    background: var(--brand-green);
  }

  /* Back */
  .back__sweep { position: absolute; inset: 0; }
  .card--back .wordmark { right: 50px; top: 48px; align-items: flex-start; }
  .card--back .wordmark__dot { width: 18px; height: 18px; }
  .card--back .wordmark__name { font-size: 26px; }
  .card--back .wordmark__tagline { font-size: 8.5px; margin-left: 28px; letter-spacing: 2px; }

  .holder {
    position: absolute; left: 14px; width: 130px; bottom: 34px;
    font-family: "Tinos", serif; color: var(--ink);
    text-align: right;
  }
  .holder__name { font-size: 18px; font-weight: 700; white-space: nowrap; }
  .holder__title { font-size: 10.5px; margin-top: 4px; white-space: nowrap; }

  .contact {
    position: absolute; right: 20px; top: 178px;
    font-family: "Tinos", serif; color: var(--ink);
    font-size: 13px; line-height: 21px;
    list-style: none;
  }
  .contact__item { display: flex; justify-content: flex-end; align-items: flex-start; gap: 12px; }
  .contact__text { text-align: right; }
  .contact__icon { width: 14px; height: 14px; margin-top: 3px; flex: none; }
</style>
</head>
<body>

  <section class="card card--front" aria-label="Card front">
    <div class="wordmark">
      <div class="wordmark__row">
        <span class="wordmark__dot"></span>
        <span class="wordmark__name">korvantareach</span>
      </div>
      <span class="wordmark__tagline">Internet Marketing Strategies</span>
    </div>
    <div class="front__rule"></div>
    <div class="front__band"></div>
  </section>

  <section class="card card--back" aria-label="Card back">
    <svg class="back__sweep" viewBox="0 0 560 320" width="560" height="320" aria-hidden="true">
      <path d="M0 0 H302 Q176 120 164 320 H0 Z" fill="var(--ink)"/>
      <path d="M0 0 H286 Q162 118 150 320 H0 Z" fill="var(--paper)"/>
      <path d="M0 0 H268 Q150 116 140 320 H0 Z" fill="var(--brand-green)"/>
    </svg>

    <div class="wordmark">
      <div class="wordmark__row">
        <span class="wordmark__dot"></span>
        <span class="wordmark__name">korvantareach</span>
      </div>
      <span class="wordmark__tagline">Internet Marketing Strategies</span>
    </div>

    <div class="holder">
      <div class="holder__name">Gareth Pennock</div>
      <div class="holder__title">Internet Marketing Strategist</div>
    </div>

    <ul class="contact">
      <li class="contact__item">
        <span class="contact__text">(555) 813-2064</span>
        <svg class="contact__icon" viewBox="0 0 16 16" aria-label="Phone"><path fill="var(--brand-blue)" d="M3.5 1.5l2.5 0 1 3.5-1.6 1.2a9 9 0 0 0 4.4 4.4L11 9l3.5 1v2.5c0 1-1 2-2 2A11 11 0 0 1 1.5 3.5c0-1 1-2 2-2z"/></svg>
      </li>
      <li class="contact__item">
        <span class="contact__text">gareth@korvantareach.com</span>
        <svg class="contact__icon" viewBox="0 0 16 16" aria-label="Email"><rect x="1" y="3" width="14" height="10" fill="var(--brand-blue)"/><path d="M1.5 3.5 8 9l6.5-5.5" stroke="#fff" stroke-width="1.3" fill="none"/></svg>
      </li>
      <li class="contact__item">
        <span class="contact__text">2156 N. Halvern Ave., Ste. 118<br>Maplecrest, Nevada 89047</span>
        <svg class="contact__icon" viewBox="0 0 16 16" aria-label="Address"><path fill="var(--brand-blue)" d="M8 1a5 5 0 0 1 5 5c0 3.5-5 9-5 9S3 9.5 3 6a5 5 0 0 1 5-5z"/><circle cx="8" cy="6" r="1.8" fill="#fff"/></svg>
      </li>
      <li class="contact__item">
        <span class="contact__text">www.korvantareach.com</span>
        <svg class="contact__icon" viewBox="0 0 16 16" aria-label="Website"><circle cx="8" cy="8" r="7" fill="var(--brand-blue)"/><path d="M1 8h14M8 1c-3 3.5-3 10.5 0 14M8 1c3 3.5 3 10.5 0 14" stroke="#fff" stroke-width="1" fill="none"/></svg>
      </li>
    </ul>
  </section>

</body>
</html>
```